Postcard Marketing Design

We need a postcard design for a screen printing and embroidery business named Tolliver's Screen Printing & Embroidery LLC. We are looking to actively market to local businesses and schools. I've attached our company logo to help with coloring theme and would like to see the logo implemented somewhere in design. The provided logo can be altered and is merely a baseline. We would like the design to have T'shirts, Sweatshirts, Hats, and a promotional item such as a lanyard. Maybe with a basic design on each that states "your logo here" or something along those lines.

Target Market(s)

local school's and businesses

Industry/Entity Type

Screen Printing

```html
<!DOCTYPE html>
<html lang="en">
<head>
<meta charset="utf-8">
<title>Tolliver's Screen Printing &amp; Embroidery – Postcard</title>
<link href="https://fonts.googleapis.com/css2?family=Libre+Baskerville:wght@700&family=Exo+2:wght@400;500;600;700&display=swap" rel="stylesheet">
<style>
  :root {
    --page-bg: #34373c;
    --card-bg: #f1f2f4;
    --brand-blue: #3a55b4;
    --band-blue: #1b8fe0;
    --band-blue-light: #43b2f2;
    --brand-red: #e0202a;
    --ink: #1a1a1a;
    --ink-soft: #2a2a35;
    --rule-blue: #2f4fb0;
  }
  * { margin: 0; padding: 0; box-sizing: border-box; }
  html, body { width: 1200px; height: 901px; overflow: hidden; }
  body { background: var(--page-bg); position: relative; }

  .postcard {
    position: absolute; left: 50px; top: 155px;
    width: 1100px; height: 590px;
    background: linear-gradient(160deg, #ffffff 0%, var(--card-bg) 60%, #e4e6ea 100%);
    overflow: hidden;
  }

  .top-band {
    position: absolute; left: 255px; top: 0; right: 0; height: 18px;
    background: linear-gradient(90deg, #8fa3e0 0%, var(--brand-blue) 60%, #2a3f99 100%);
  }
  .top-rule {
    position: absolute; left: 255px; top: 20px; right: 0; height: 5px;
    background: var(--brand-red);
  }

  .photo-model {
    position: absolute; left: 0; top: 0; width: 422px; height: 476px;
    background: linear-gradient(135deg, #e9e9ea 0%, #ffffff 45%, #f2c9b8 75%, #e5532c 100%);
  }
  .photo-jerseys {
    position: absolute; left: 422px; top: 240px; width: 190px; height: 226px;
    background: linear-gradient(160deg, #ef5a2e 0%, #f4f4f6 55%, #2f55c4 100%);
  }

  .brand-name {
    position: absolute; left: 450px; top: 48px; width: 620px;
    display: flex; align-items: center; gap: 18px;
    font-family: "Libre Baskerville", serif; font-weight: 700; color: var(--ink);
  }
  .brand-mark {
    width: 40px; height: 40px; background: var(--brand-red); flex: none;
  }
  .brand-text { line-height: 1.05; }
  .brand-text .name { display: block; font-size: 70px; letter-spacing: -1px; }
  .brand-text .trade { display: block; font-size: 25px; margin-top: 6px; }

  .services-bar {
    position: absolute; left: 608px; top: 186px; width: 442px; height: 33px;
    background: linear-gradient(90deg, #5a74cf 0%, var(--rule-blue) 100%);
    color: #fff; font-family: "Exo 2", sans-serif; font-weight: 500;
    font-size: 25px; letter-spacing: 1px; line-height: 33px;
    padding-left: 132px;
  }
  .services-bar svg { position: absolute; left: 52px; top: -6px; }

  .service-list {
    position: absolute; right: 50px; top: 228px; width: 470px;
    font-family: "Exo 2", sans-serif; font-weight: 500; color: var(--ink-soft);
    text-transform: uppercase; text-align: right;
    font-size: 19.5px; letter-spacing: 1.6px; line-height: 26px;
  }
  .service-group { padding: 2px 0 4px; border-bottom: 3px solid var(--rule-blue); margin-bottom: 6px; }
  .service-group:last-child { border-bottom: none; }
  .service-group.indent { margin-left: 40px; }

  .bottom-rule {
    position: absolute; left: 600px; right: 0; top: 466px; height: 10px;
    background: var(--brand-red);
  }
  .bottom-band {
    position: absolute; left: 0; right: 0; top: 476px; bottom: 0;
    background: linear-gradient(180deg, var(--band-blue-light) 0%, var(--band-blue) 55%, #0f74c9 100%);
  }

  .website {
    position: absolute; left: 47px; top: 524px;
    font-family: "Exo 2", sans-serif; font-weight: 600; font-size: 29px;
    letter-spacing: 5px; color: var(--ink);
  }
  .contact {
    position: absolute; right: 40px; top: 484px; text-align: right;
    font-family: "Exo 2", sans-serif; color: var(--ink);
  }
  .contact .cta { font-size: 20px; font-weight: 500; letter-spacing: 1px; }
  .contact .phone {
    display: flex; align-items: center; justify-content: flex-end; gap: 14px;
    font-size: 38px; font-weight: 700; letter-spacing: 1px; line-height: 1.05;
  }
  .contact .email { font-size: 24px; font-weight: 500; letter-spacing: 2px; }
</style>
</head>
<body>
  <main class="postcard">
    <div class="top-band"></div>
    <div class="top-rule"></div>

    <div class="photo-model" role="img" aria-label="Photo of a model in a white printed T-shirt, with a red printed mug and an orange cap reading Your Logo Here"></div>
    <div class="photo-jerseys" role="img" aria-label="Photo of an orange sports jersey and a blue and white polo shirt, each printed with Your Logo Here"></div>

    <div class="brand-name">
      <span class="brand-mark"></span>
      <span class="brand-text">
        <span class="name">Tolliver's</span>
        <span class="trade">Screen Printing &amp; Embroidery</span>
      </span>
    </div>

    <div class="services-bar">
      <svg width="56" height="30" viewBox="0 0 56 30" aria-hidden="true">
        <polygon points="0,0 56,0 28,30" fill="#e0202a"/>
      </svg>
      Services offered
    </div>

    <div class="service-list">
      <div class="service-group">Hats, jackets, sweatshirts,<br>sweatpants, shorts, T-shirts,<br>promotional items, etc.</div>
      <div class="service-group indent">Custom order sheets to<br>make your job easier</div>
      <div class="service-group indent">Low prices guaranteed</div>
      <div class="service-group indent">Fast turnaround</div>
      <div class="service-group">All our work is done in house</div>
    </div>

    <div class="bottom-rule"></div>
    <div class="bottom-band"></div>

    <div class="website">www.tolliversllc.com</div>

    <div class="contact">
      <div class="cta">Call Us now</div>
      <div class="phone">
        <svg width="40" height="28" viewBox="0 0 40 28" aria-hidden="true">
          <rect x="1.5" y="1.5" width="37" height="25" fill="none" stroke="#1a1a1a" stroke-width="2.5"/>
          <path d="M9 11 q11 -7 22 0 l-2 3 h-4 l-1 -2 h-8 l-1 2 h-4 z" fill="#1a1a1a"/>
          <rect x="12" y="15" width="16" height="7" fill="#1a1a1a"/>
        </svg>
        555-014-2290
      </div>
      <div class="email">orders@tolliversprint.com</div>
    </div>
  </main>
</body>
</html>
```